Porchlight Gin - Label for new Gin bottle

I am looking for a bottle label for our small batch, handcrafted Gin. We are located in the bay-side city of Frankston (Victoria, Australia). I know I want more of a serious label but am torn between traditional or modern styling.

Label to include;
• Porchlight GIN (name)
• Hand Crafted
• Small Batch
• 40% Vol

Using 700ml VANTA Spirit Bottle - Cork

Requirements
Must have
• Name; Porchlight Gin
Method: Hand Crafted
Batch Size; Small Batch
Alc; 40% Vol
Nice to have
• Maybe a coastal/seaside reference or reference to distilling.

```html
<!DOCTYPE html>
<html lang="en">
<head>
<meta charset="utf-8">
<title>Porchlight Gin – Label</title>
<link rel="stylesheet" href="https://fonts.googleapis.com/css2?family=Rye&family=Roboto+Slab:wght@700;800&display=swap">
<style>
  :root {
    --page: #f5f5f5;
    --label-top: #d9d3ca;
    --label-mid: #cfc7bb;
    --sepia-light: #c8bba5;
    --sepia-mid: #a58d68;
    --sepia-dark: #7a6340;
    --ink: #2b2b2b;
    --ink-brown: #4a3a26;
    --echo: #f3efe8;
  }
  html, body {
    margin: 0;
    width: 1155px;
    height: 1200px;
    overflow: hidden;
    background: var(--page);
  }
  .label {
    position: absolute;
    left: 127px;
    top: 172px;
    width: 900px;
    height: 856px;
    overflow: hidden;
    background: linear-gradient(180deg, var(--label-top) 0%, var(--label-mid) 45%, var(--sepia-light) 100%);
    text-align: center;
  }
  .coastal-scene {
    position: absolute;
    left: 0;
    right: 0;
    top: 360px;
    bottom: 0;
    background:
      linear-gradient(180deg, rgba(122,99,64,0.85) 0%, rgba(140,115,78,0.7) 30%, rgba(190,176,150,0.55) 55%, rgba(200,188,166,0.6) 100%),
      linear-gradient(90deg, var(--sepia-dark) 0%, var(--sepia-mid) 35%, var(--sepia-light) 100%);
  }
  .method {
    position: absolute;
    top: 66px;
    left: 0;
    right: 0;
    font: 800 30px/1 "Roboto Slab", serif;
    letter-spacing: 2px;
    color: var(--ink);
  }
  .method .rule {
    display: inline-block;
    width: 26px;
    height: 4px;
    background: var(--ink);
    vertical-align: middle;
    margin: 0 20px;
  }
  .batch {
    position: absolute;
    left: 0;
    right: 0;
    font: 700 22px/1 "Roboto Slab", serif;
    letter-spacing: 1.5px;
  }
  .batch--main { top: 128px; color: var(--ink); }
  .batch--echo { top: 164px; color: var(--echo); }
  .brand-name {
    position: absolute;
    top: 250px;
    left: 0;
    right: 0;
    margin: 0;
    font: 400 94px/1 "Rye", serif;
    color: var(--ink);
    letter-spacing: 1px;
  }
  .category {
    position: absolute;
    top: 600px;
    left: 0;
    right: 0;
    font: 400 84px/1 "Rye", serif;
    color: var(--ink);
    letter-spacing: 6px;
  }
  .abv {
    position: absolute;
    top: 770px;
    left: 0;
    right: 0;
    font: 700 34px/1 "Roboto Slab", serif;
    color: var(--ink-brown);
    letter-spacing: 2px;
  }
</style>
</head>
<body>
  <main class="label">
    <div class="coastal-scene" role="img" aria-label="Sepia photograph of a bayside coastline with a clubhouse on the shore, tree-covered cliffs and waves"></div>
    <div class="method"><span class="rule"></span>HAND CRAFTED<span class="rule"></span></div>
    <div class="batch batch--main">SMALL BATCH</div>
    <div class="batch batch--echo">SMALL BATCH</div>
    <h1 class="brand-name">PORCHLIGHT</h1>
    <div class="category">GIN</div>
    <div class="abv">40% VOL</div>
  </main>
</body>
</html>
```